Rinaldo's Top Paw Haven 555

I'm a Veterinary Assitant over 20 year experience in West Los Angeles with wealthy clients . I just open a business which will include Petsitting in my house dogs and cats only visiting clients house's stay overnights , transporting animal to the hospital or physical therapy
Services including small % of dog walking , nail trim , ear cleaning , giving medication , Sq fluids , passive of range and motion post surgery many of my clients is all referral from veterinary's either general practice or specialist . I already got the
Ficstitious Bussines Statement going and in the process of getting a Petsitting insurance with a good cover also I will have a website with many clients testimonies and Veterinary references . Hope this is enough information . Thanks Rinaldo feel free to contact me with any questions

Target Market(s)

Pet Owners that are pet lovers but really busy not able to give medication
Or care for the pet

Industry/Entity Type

Business

Contact Information for Business Card

Bussines based on love and care for pets wellbeing driven by trust and reliability .

Font styles to use
Serif
Decorative

Colors
00a990
33b8a4
30b7a3

Requirements
Must have
• The bussines name ,
• Over 20 years experience as a Veterinay Assitant
• Pet Sitting / In Home Care / Transportation
• Licensed and Insured
• Phone 310- 647-3918
• Website : rinaldotoppawhaven555.com
• email: info@rinaldotoppawhaven555.com
Nice to have
• Please give me a idea
Should not have
• no address on the business card .

```html
<!DOCTYPE html>
<html lang="en">
<head>
<meta charset="utf-8">
<title>Rinaldo's Top Paw Haven 555 – Business Card</title>
<link href="https://fonts.googleapis.com/css2?family=Lato:wght@400;700;900&display=swap" rel="stylesheet">
<style>
  :root{
    --teal:#00a990;
    --teal-soft:#30b7a3;
    --tan:#d9c2a0;
    --ink:#2a2a2a;
    --paper:#ffffff;
    --backdrop:#e9e7e3;
  }
  *{box-sizing:border-box;margin:0;padding:0}
  html,body{width:1200px;height:901px;overflow:hidden;background:var(--backdrop)}
  body{font-family:'Lato',sans-serif;color:var(--ink);position:relative}

  .card{position:absolute;left:270px;width:660px;height:377px;background:var(--paper);
        box-shadow:0 6px 18px rgba(0,0,0,.18);overflow:hidden}
  .card--front{top:36px}
  .card--back{top:488px}

  .brand{display:flex;align-items:center;gap:12px}
  .brand__dot{width:22px;height:22px;border-radius:50%;background:var(--teal);flex:none}
  .brand__name{font-weight:900;color:var(--teal);font-size:34px;white-space:nowrap}

  /* front */
  .card--front .brand{position:absolute;left:0;right:0;top:120px;justify-content:center}
  .services{position:absolute;left:0;right:0;top:196px;text-align:center;font-size:16.5px;line-height:1.6}
  .services .sep{color:var(--teal);margin:0 6px}

  /* back */
  .card--back .brand{position:absolute;left:40px;top:40px}
  .card--back .brand__name{font-size:28px}
  .contacts{position:absolute;left:40px;top:104px;list-style:none;font-size:16px;line-height:1.6}
  .contacts li{display:flex;align-items:center;gap:12px}
  .contacts svg{width:14px;height:14px;flex:none;fill:var(--teal)}

  .holder{position:absolute;right:44px;top:150px;text-align:left}
  .holder__name{color:var(--teal);font-size:26px;font-weight:700}
  .holder__title{font-size:17px;margin-bottom:14px}
  .holder__facts{list-style:none;font-size:17px;line-height:1.4}

  .swoosh{position:absolute;left:0;top:0;width:660px;height:377px}
</style>
</head>
<body>

  <section class="card card--front" aria-label="Card front">
    <div class="brand">
      <span class="brand__dot"></span>
      <span class="brand__name">Rinaldo's Top Paw Haven 555</span>
    </div>
    <p class="services">
      Pet Sitting<span class="sep">•</span>In Home Care<span class="sep">•</span>Transportation<br>
      Dog Walking<span class="sep">•</span>Nail Trim<span class="sep">•</span>Ear Cleaning<span class="sep">•</span>Giving medication<br>
      Sq fluids to cats on renal failure<span class="sep">•</span>Passive of range motion post surgery
    </p>
  </section>

  <section class="card card--back" aria-label="Card back">
    <svg class="swoosh" viewBox="0 0 660 377" aria-hidden="true">
      <path d="M0 215 C50 260 100 320 140 377 L0 377 Z" fill="var(--tan)"/>
      <path d="M85 250 C200 330 420 372 660 300 L660 377 L210 377 C160 335 120 295 85 250 Z" fill="var(--teal)"/>
    </svg>

    <div class="brand">
      <span class="brand__dot"></span>
      <span class="brand__name">Rinaldo's Top Paw Haven 555</span>
    </div>

    <ul class="contacts">
      <li><svg viewBox="0 0 16 16"><path d="M3 1l3 3-2 2c1 2 3 4 6 6l2-2 3 3-2 2C7 15 1 9 1 3z"/></svg>310- 647-3918</li>
      <li><svg viewBox="0 0 16 16"><path d="M4 0h8v16H4z M5 2v10h6V2z" fill-rule="evenodd"/></svg>310- 555-0142</li>
      <li><svg viewBox="0 0 16 16"><path d="M0 3h16v10H0z M1 4l7 5 7-5z" fill-rule="evenodd"/></svg>info@rinaldotoppawhaven555.com</li>
      <li><svg viewBox="0 0 16 16"><circle cx="8" cy="8" r="7.5"/></svg>www.rinaldotoppawhaven555.com</li>
    </ul>

    <div class="holder">
      <p class="holder__name">Rinaldo Vestri</p>
      <p class="holder__title">Veterinary Assitant</p>
      <ul class="holder__facts">
        <li>Over 20 years experience</li>
        <li>Licensed and Insured</li>
      </ul>
    </div>
  </section>

</body>
</html>
```